KMW Plumbing and Roofing

design a fresh modern card for a young plumbing business looking to break into the market.
Must include the logo in the attached file
Bryce Olmo Verity
Phone number 0413962840
Vic Licence no 63194
email......

New Homes & Renovations
General Plumbing & Maintenance
Solar Hot Water Units
Roofing & Guttering (new and replacement)

Industry/Entity Type

Business

```html
<!DOCTYPE html>
<html lang="en">
<head>
<meta charset="utf-8">
<title>KMW Plumbing and Roofing – Business Card</title>
<link rel="stylesheet" href="https://fonts.googleapis.com/css2?family=Montserrat:wght@400;500;600;700&display=swap">
<style>
  :root {
    --bg: #3b423f;
    --paper: #ffffff;
    --paper-shade: #eef0f1;
    --blue-deep: #0d4a78;
    --blue-mid: #0b6f92;
    --blue-bright: #1192ad;
    --navy: #123a5c;
    --gold: #e0a93a;
    --gold-dark: #c9912a;
    --muted: #b9cbd6;
  }
  * { box-sizing: border-box; margin: 0; padding: 0; }
  html, body { width: 1200px; height: 900px; overflow: hidden; }
  body {
    background: var(--bg);
    font-family: "Montserrat", sans-serif;
    display: flex; flex-direction: column; align-items: center; justify-content: center;
    gap: 40px;
  }
  .card {
    width: 680px; height: 388px;
    background: var(--paper);
    position: relative; overflow: hidden;
    box-shadow: 0 12px 30px rgba(0,0,0,.35);
  }
  .brand {
    display: flex; align-items: center; gap: 14px;
    color: var(--navy); font-weight: 700;
  }
  .brand-dot {
    width: 34px; height: 34px; border-radius: 50%;
    background: var(--gold);
  }
  .brand-name { font-size: 26px; letter-spacing: .2px; }

  /* front */
  .card-front .brand { position: absolute; left: 40px; top: 52px; }
  .card-front .band { position: absolute; inset: 0; }
  .front-info {
    position: absolute; left: 40px; right: 40px; top: 196px; bottom: 30px;
    display: flex; justify-content: space-between; color: #fff;
  }
  .person-name { color: var(--gold); font-size: 21px; font-weight: 500; letter-spacing: 2px; text-transform: uppercase; }
  .person-role { color: var(--muted); font-size: 12px; font-weight: 600; letter-spacing: 1.5px; text-transform: uppercase; margin-top: 6px; }
  .licence { color: var(--muted); font-size: 16px; letter-spacing: 1.5px; margin-top: 30px; line-height: 1.45; }
  .licence .holder { text-transform: uppercase; }
  .contact { font-size: 15px; letter-spacing: 1.2px; line-height: 1.5; padding-right: 6px; }
  .contact-list { list-style: none; margin-top: 14px; font-size: 14px; }
  .contact-list li { display: flex; align-items: center; gap: 12px; line-height: 1.55; }
  .contact-list .url { text-transform: uppercase; font-size: 12.5px; }
  .icon { width: 14px; height: 14px; flex: none; }

  /* back */
  .card-back .brand { position: absolute; left: 50%; top: 110px; transform: translateX(-50%); }
  .card-back .brand-name { font-size: 32px; }
  .card-back .brand-dot { width: 40px; height: 40px; }
  .divider { position: absolute; left: 40px; right: 40px; top: 262px; height: 1px; background: var(--blue-deep); opacity: .7; }
  .services {
    position: absolute; left: 40px; right: 40px; top: 280px;
    display: grid; grid-template-columns: auto auto; column-gap: 22px; row-gap: 10px;
    list-style: none; color: var(--blue-deep); font-size: 14px; font-weight: 500;
    letter-spacing: .6px; text-transform: uppercase; justify-content: center;
  }
  .services li { display: flex; align-items: center; gap: 6px; }
  .tick { width: 13px; height: 13px; flex: none; }
</style>
</head>
<body>
  <section class="card card-front">
    <svg class="band" viewBox="0 0 680 388" preserveAspectRatio="none" aria-hidden="true">
      <defs>
        <radialGradient id="blueGlow" cx="62%" cy="55%" r="70%">
          <stop offset="0" stop-color="var(--blue-bright)"/>
          <stop offset=".55" stop-color="var(--blue-mid)"/>
          <stop offset="1" stop-color="var(--blue-deep)"/>
        </radialGradient>
      </defs>
      <rect width="680" height="160" fill="var(--paper-shade)" opacity=".5"/>
      <path d="M0 164 L70 164 L82 176 L94 164 L680 150 L680 388 L0 388 Z" fill="url(#blueGlow)"/>
      <path d="M0 164 L70 164 L82 176 L94 164 L680 150" fill="none" stroke="var(--gold)" stroke-width="3"/>
    </svg>
    <div class="brand">
      <span class="brand-dot"></span>
      <span class="brand-name">KMW Plumbing and Roofing</span>
    </div>
    <div class="front-info">
      <div class="identity">
        <p class="person-name">Daniel Hargrove</p>
        <p class="person-role">President</p>
        <p class="licence"><span class="holder">Bryce Olmo Verity</span><br>Vic Licence no 63194</p>
      </div>
      <div class="contact">
        <p>72 Keller Road<br>Westbridge, VIC 3172</p>
        <ul class="contact-list">
          <li><svg class="icon" viewBox="0 0 14 14"><rect width="14" height="14" rx="2" fill="var(--gold)"/><rect x="4.5" y="2.5" width="5" height="9" rx="1" fill="none" stroke="var(--blue-deep)" stroke-width="1.3"/></svg>041-396-2840</li>
          <li><svg class="icon" viewBox="0 0 14 14"><rect width="14" height="14" rx="2" fill="var(--gold)"/><rect x="2.5" y="4" width="9" height="6" fill="none" stroke="var(--blue-deep)" stroke-width="1.2"/><path d="M2.5 4 L7 7.5 L11.5 4" fill="none" stroke="var(--blue-deep)" stroke-width="1.2"/></svg>info@kmwplumbing.com.au</li>
          <li class="url"><svg class="icon" viewBox="0 0 14 14"><rect width="14" height="14" rx="2" fill="var(--gold)"/><circle cx="7" cy="7" r="4.3" fill="none" stroke="var(--blue-deep)" stroke-width="1.1"/><path d="M2.7 7 H11.3 M7 2.7 V11.3" stroke="var(--blue-deep)" stroke-width="1"/></svg>www.kmwplumbing.com.au</li>
        </ul>
      </div>
    </div>
  </section>

  <section class="card card-back">
    <div class="brand">
      <span class="brand-dot"></span>
      <span class="brand-name">KMW Plumbing and Roofing</span>
    </div>
    <div class="divider"></div>
    <ul class="services">
      <li><svg class="tick" viewBox="0 0 13 13"><path d="M1.5 7 L5 10.5 L11.5 2" fill="none" stroke="var(--gold-dark)" stroke-width="2.2"/></svg>New Homes &amp; Renovations</li>
      <li><svg class="tick" viewBox="0 0 13 13"><path d="M1.5 7 L5 10.5 L11.5 2" fill="none" stroke="var(--gold-dark)" stroke-width="2.2"/></svg>General Plumbing &amp; Maintenance</li>
      <li><svg class="tick" viewBox="0 0 13 13"><path d="M1.5 7 L5 10.5 L11.5 2" fill="none" stroke="var(--gold-dark)" stroke-width="2.2"/></svg>Solar Hot Water Units</li>
      <li><svg class="tick" viewBox="0 0 13 13"><path d="M1.5 7 L5 10.5 L11.5 2" fill="none" stroke="var(--gold-dark)" stroke-width="2.2"/></svg>Roofing &amp; Guttering (New and Replacement)</li>
    </ul>
  </section>
</body>
</html>
```